Business Card design for a mobile solutions company

- we are a mobile telecommunications company focusing on mobile content and solutions
- we are based in Malaysia however operate a regional business
- attached is our company logo and current business card design
- please try to incorporate the "cubes" into the design

our company philosophy is dynamic and outgoing. we are a lean team of less than 50, but we have strong roots in the mobile industry in Asia and we like to challenge ourselves by taking on larger projects.

we love joint ventures and working with partners to find the right solutions for our clients

*please feel free to modify our logo (typeface etc)
**we would like to keep the 3 cube design for the logo, but I would love to see different versions of it
Updates

some of the designs are great and I think our logo (especially the typeface used for the words) doesn't look good. please feel free to update the logo but try to keep the cubes, you are free to modify the cubes and update them.

Reason: looking for more design please

Industry/Entity Type

Telecommunications

Font styles to use
Sans Serif

```html
<!DOCTYPE html>
<html lang="en">
<head>
<meta charset="utf-8">
<title>Luma Grid – Business Card</title>
<link href="https://fonts.googleapis.com/css2?family=Open+Sans:wght@800&family=Exo+2:wght@400;600&display=swap" rel="stylesheet">
<style>
  :root{
    --backdrop:#d9d3c4;
    --paper:#ffffff;
    --ink:#111111;
    --navy:#23272f;
    --orange:#f0a13a;
    --red:#d9453d;
    --blue:#2f6fb5;
    --muted:#b9bdc6;
    --light:#e6e8ec;
    --soft-1:#f1eef3;
    --soft-2:#e4e9e4;
  }
  *{box-sizing:border-box;margin:0;padding:0}
  html,body{width:1200px;height:800px;overflow:hidden}
  body{background:var(--backdrop);position:relative;font-family:"Exo 2",sans-serif}

  .card{position:absolute;width:560px;height:320px;overflow:hidden;
        box-shadow:0 6px 18px rgba(0,0,0,.18)}

  .brand-mark{display:block;background:var(--orange);flex:none}
  .brand-name{font-family:"Open Sans",sans-serif;font-weight:800;color:var(--ink);
        letter-spacing:.5px;line-height:1;white-space:nowrap}

  /* ---------- front ---------- */
  .card--front{left:80px;top:60px;background:var(--paper)}
  .front__texture{position:absolute;inset:0;
        background:linear-gradient(135deg,var(--soft-1) 0%,#f6f2ea 35%,var(--soft-2) 70%,#efe9f1 100%)}
  .front__stripes{position:absolute;top:0;bottom:0;left:410px;display:flex}
  .front__stripes span{width:20px;height:100%}
  .stripe--orange{background:var(--orange)}
  .stripe--red{background:var(--red)}
  .stripe--blue{background:var(--blue)}
  .front__brand{position:absolute;left:36px;bottom:44px;display:flex;align-items:center;gap:12px}
  .front__brand .brand-mark{width:34px;height:34px}
  .front__brand .brand-name{font-size:44px}

  /* ---------- back ---------- */
  .card--back{left:560px;top:420px;background:var(--paper)}
  .back__shapes{position:absolute;inset:0}
  .back__brand{position:absolute;left:60px;top:40px;display:flex;align-items:center;gap:18px}
  .back__brand .brand-mark{width:56px;height:56px}
  .back__brand .brand-name{font-size:38px}

  .contact{position:absolute;left:380px;top:180px;list-style:none;color:var(--light);font-size:11.5px;line-height:17px}
  .contact li{display:flex;align-items:center;gap:6px}
  .contact svg{width:13px;height:13px;flex:none}

  .person{position:absolute;left:34px;top:228px}
  .person__name{font-weight:600;font-size:21px;color:var(--orange);line-height:1}
  .person__title{font-size:10.5px;color:var(--light);margin-top:2px}
  .address{position:absolute;left:100px;top:270px;font-size:10.5px;color:var(--muted);line-height:14px}

  .back__bar{position:absolute;left:0;right:0;bottom:0;height:7px;display:flex}
  .back__bar span{flex:1}
</style>
</head>
<body>

<section class="card card--front" aria-label="Card front">
  <div class="front__texture" role="img" aria-label="Faint scattered pastel cubes background"></div>
  <div class="front__stripes">
    <span class="stripe--orange"></span><span class="stripe--red"></span><span class="stripe--blue"></span>
  </div>
  <div class="front__brand">
    <span class="brand-mark"></span>
    <span class="brand-name">LUMA GRID</span>
  </div>
</section>

<section class="card card--back" aria-label="Card back">
  <svg class="back__shapes" width="560" height="320" viewBox="0 0 560 320" aria-hidden="true">
    <polygon points="0,218 330,202 440,134 560,128 560,320 0,320" fill="var(--navy)"/>
    <polygon points="60,216 440,132 330,202" fill="var(--orange)"/>
  </svg>

  <div class="back__brand">
    <span class="brand-mark"></span>
    <span class="brand-name">LUMA GRID</span>
  </div>

  <ul class="contact">
    <li>
      <svg viewBox="0 0 14 14"><rect width="14" height="14" rx="3" fill="var(--orange)"/><path d="M4 4h6v2H9V5H5v1H4zM4 7h6v3H4z" fill="#23272f"/></svg>
      +60 3 555 0142
    </li>
    <li>
      <svg viewBox="0 0 14 14"><rect width="14" height="14" rx="3" fill="var(--orange)"/><rect x="5" y="3" width="4" height="8" rx="1" fill="#23272f"/></svg>
      +62 855 5550199
    </li>
    <li>
      <svg viewBox="0 0 14 14"><rect width="14" height="14" rx="3" fill="var(--orange)"/><rect x="3" y="4.5" width="8" height="5" fill="#23272f"/><path d="M3 4.5l4 3 4-3" stroke="var(--orange)" fill="none"/></svg>
      adrian@lumagrid.com.my
    </li>
  </ul>

  <div class="person">
    <p class="person__name">Adrian tan</p>
    <p class="person__title">chief Marketing Officer</p>
  </div>
  <p class="address">luma grid SDN BHD unit 5-1 level 5 block 2 the meridian<br>taman seri No.4 jalan cempaka 58000 kuala lumpur</p>

  <div class="back__bar">
    <span class="stripe--blue"></span><span class="stripe--red"></span><span class="stripe--orange"></span>
  </div>
</section>

</body>
</html>
```